Zelno Vigor Iron Tempo Multi Vitamin Label Design

We need a label design for our Sports Performance Daily Multi Vitamin specially created and branded for our Zelno Vigor line for the University of Calvoria. The feel is edgy, sports nutrition. Two logos need to be incorporated... Zelno and the Collective Logo attached. The colors should be the official colors of the University of Calvoria. The font may also be the Georgia font... or the Zelno font. Or any font. A hydration product will also be created later on...so this label design may be used on many products. Please utilize the collective logo similar to the use in the attached photo. No official trademark items from the University of Calvoria should be used. Attached is also an image if the bottle (white) that will be used for the vitamin. Please use red, black, grey, white. We are looking for the front design only right now and once selected, will work on the nutrition/back label portion with the artist.

```html
<!DOCTYPE html>
<html lang="en">
<head>
<meta charset="UTF-8">
<title>Zelno Vigor Sport Performance Label</title>
<link rel="stylesheet" href="https://fonts.googleapis.com/css2?family=Anton&family=Montserrat:wght@600;800&display=swap">
<style>
  :root {
    --page: #e4e4e4;
    --red: #e01d24;
    --red-dark: #a8161b;
    --red-deep: #7d1216;
    --black: #1a1a1a;
    --panel: #262626;
    --silver: #c9c9cc;
    --silver-dark: #8e8e92;
    --white: #ffffff;
  }
  * { margin: 0; padding: 0; box-sizing: border-box; }
  html, body { width: 1200px; height: 1200px; overflow: hidden; background: var(--page); }
  .canvas { position: relative; width: 1200px; height: 1200px; }
  .label-shape { position: absolute; left: 0; top: 0; }
  .label-text { position: absolute; left: 0; top: 0; width: 1200px; height: 1200px; }

  .collective {
    position: absolute; top: 300px; left: 0; width: 1200px;
    display: flex; justify-content: center; align-items: center; gap: 16px;
    font-family: "Montserrat", sans-serif; font-weight: 800;
    font-size: 30px; letter-spacing: 4px; color: var(--white);
  }
  .collective-dot { width: 22px; height: 22px; border-radius: 50%; background: var(--red); }

  .sport {
    position: absolute; top: 400px; left: 0; width: 1200px; text-align: center;
    font-family: "Anton", sans-serif; font-size: 230px; line-height: 1;
    letter-spacing: 6px;
    background: linear-gradient(90deg, var(--red-dark), var(--red) 50%, var(--red-dark));
    -webkit-background-clip: text; background-clip: text; color: transparent;
  }
  .performance {
    position: absolute; top: 655px; left: 0; width: 1200px; text-align: center;
    font-family: "Anton", sans-serif; font-size: 92px; line-height: 1; letter-spacing: 3px;
    background: linear-gradient(90deg, var(--silver-dark), var(--white) 55%, var(--silver-dark));
    -webkit-background-clip: text; background-clip: text; color: transparent;
  }
  .product-type {
    position: absolute; top: 770px; left: 0; width: 1200px; text-align: center;
    font-family: "Montserrat", sans-serif; font-weight: 800; font-size: 44px;
    letter-spacing: 1px; color: var(--red-deep);
  }
  .brand {
    position: absolute; top: 835px; left: 0; width: 1200px; text-align: center;
    font-family: "Montserrat", sans-serif; font-weight: 800; font-size: 76px;
    letter-spacing: 6px; color: var(--white);
  }
  .footnote {
    position: absolute; top: 958px;
    font-family: "Montserrat", sans-serif; font-weight: 600; font-size: 17px; color: var(--white);
  }
  .footnote-left { left: 70px; }
  .footnote-right { right: 70px; }
  .footnote strong { font-weight: 800; }
</style>
</head>
<body>
<div class="canvas">
  <svg class="label-shape" width="1200" height="1200" viewBox="0 0 1200 1200">
    <defs>
      <linearGradient id="redBand" x1="0" y1="0" x2="1" y2="0">
        <stop offset="0" stop-color="#c3181e"/>
        <stop offset="0.5" stop-color="#ef2a30"/>
        <stop offset="1" stop-color="#c3181e"/>
      </linearGradient>
      <linearGradient id="panelFill" x1="0" y1="0" x2="1" y2="0">
        <stop offset="0" stop-color="#141414"/>
        <stop offset="0.5" stop-color="#2c2c2c"/>
        <stop offset="1" stop-color="#141414"/>
      </linearGradient>
    </defs>
    <rect class="band" x="30" y="205" width="1140" height="800" fill="url(#redBand)"/>
    <path class="panel-frame" d="M30 262 H250 L290 222 H910 L950 262 H1170 V948 H950 L910 988 H290 L250 948 H30 Z"
          fill="none" stroke="var(--silver)" stroke-width="6"/>
    <path class="panel" d="M30 272 H254 L294 232 H906 L946 272 H1170 V938 H946 L906 978 H294 L254 938 H30 Z"
          fill="url(#panelFill)"/>
  </svg>

  <div class="label-text">
    <div class="collective"><span class="collective-dot"></span>REDLINE COLLECTIVE</div>
    <div class="sport">SPORT</div>
    <div class="performance">PERFORMANCE</div>
    <div class="product-type">DAILY MULTI VITAMIN</div>
    <div class="brand">ZELNO</div>
    <div class="footnote footnote-left">DIETARY SUPPLEMENT</div>
    <div class="footnote footnote-right"><strong>60</strong> VEGGIE CAPSULES</div>
  </div>
</div>
</body>
</html>
```